BrightLoft Aerial Business Card Design

I need a business card designed around my logo/name. I don't mind if you alter the logo slightly or have an idea to make it work different than it is. I also need a card that identifies my business by looking at the card. I am a drone operator who takes photo and video to be used for real estate listings, and mapping for construction.

Target Market(s)

Real Estate and Construction

Industry/Entity Type

Business

Contact Information for Business Card

I'd like it to be simple, but say a lot, have the "S" logo somewhere, but not doesn't have to prominent.

Font styles to use
Serif
Sans Serif

Colors
0792cd
00a990
fbed22
ffc214
f78f20
f69356
ed232b
000000
0456a4

Requirements
Must have
• "We'll get the shot you need"
• Marcus Delaney
• Pilot / Owner
• 18 Pelmont Ridge
• Alder Crossing, CT 06000
• FAA 107 # 5164273
• Insured
• Rotor Academy Certified
• (203) 555-0147
• brightloftaerial@mailbox-example.com
• brightloftaerial-example.com
Nice to have
• Something that hints to the client that I fly drones to take photos--I use a Veltro Hawk 3, which kind of looks like a "Y" when it is flying--I've included a few pics.
Should not have
• more than 3 colors.

```html
<!DOCTYPE html>
<html lang="en">
<head>
<meta charset="utf-8">
<title>BrightLoft Aerial – Business Card</title>
<link rel="stylesheet" href="https://fonts.googleapis.com/css2?family=Lato:ital,wght@0,400;0,700;0,900;1,400&display=swap">
<style>
  :root {
    --brand-blue: #0456a4;
    --sky-blue: #0792cd;
    --accent-red: #ed232b;
    --ink-blue: #1d63b0;
    --paper: #ffffff;
    --sky-top: #b9d2ea;
    --sky-mid: #dbe8f4;
    --backdrop: #e9ecef;
    --drone-grey: #9ba4ad;
  }
  * { box-sizing: border-box; margin: 0; padding: 0; }
  html, body { width: 1200px; height: 780px; overflow: hidden; }
  body {
    background: var(--backdrop);
    font-family: "Lato", sans-serif;
    position: relative;
  }

  .card {
    position: absolute;
    border-radius: 22px;
    overflow: hidden;
    background: var(--paper);
    box-shadow: 0 10px 28px rgba(0,0,0,0.18);
  }

  /* Front card */
  .card-front {
    left: 110px; top: 95px;
    width: 350px; height: 590px;
  }
  .front-sky {
    position: absolute; left: 0; top: 0; right: 0; height: 330px;
    background: linear-gradient(180deg, var(--sky-top) 0%, var(--sky-mid) 45%, var(--paper) 100%);
  }
  .front-brand {
    position: absolute; left: 0; right: 0; top: 92px;
    display: flex; flex-direction: column; align-items: center; gap: 14px;
  }
  .brand-dot {
    width: 58px; height: 58px; border-radius: 50%;
    background: var(--sky-blue);
    flex: none;
  }
  .brand-name {
    font-weight: 900; font-size: 30px; color: var(--brand-blue);
    letter-spacing: 1px; white-space: nowrap;
  }
  .front-info {
    position: absolute; left: 0; right: 0; top: 250px;
    text-align: center;
  }
  .person-name { font-weight: 900; font-size: 28px; color: var(--ink-blue); }
  .person-role { font-size: 18px; color: var(--accent-red); margin-top: 2px; }
  .address { font-size: 17px; color: var(--ink-blue); margin-top: 14px; line-height: 1.3; }
  .contact-list { margin: 14px 24px 0; list-style: none; }
  .contact-item {
    border-top: 1px solid rgba(237,35,43,0.45);
    padding: 6px 0 5px;
    display: flex; flex-direction: column; align-items: center; gap: 3px;
    font-size: 15px; color: var(--ink-blue);
    white-space: nowrap;
  }
  .contact-item svg { width: 14px; height: 14px; }
  .front-band {
    position: absolute; left: 0; right: 0; bottom: 0; height: 34px;
    background: var(--brand-blue);
    border-top: 3px solid var(--accent-red);
  }

  /* Back card */
  .card-back {
    left: 520px; top: 215px;
    width: 600px; height: 360px;
  }
  .back-sky {
    position: absolute; inset: 0;
    background: linear-gradient(160deg, var(--sky-top) 0%, var(--sky-mid) 55%, #eef3f8 100%);
  }
  .back-drone {
    position: absolute; right: 40px; top: 50px;
    width: 270px; height: 250px; border-radius: 14px;
    background: radial-gradient(ellipse at center, var(--drone-grey) 0%, rgba(155,164,173,0.45) 55%, rgba(155,164,173,0) 75%);
  }
  .back-brand {
    position: absolute; left: 44px; top: 60px;
    display: flex; align-items: center; gap: 12px;
  }
  .back-brand .brand-dot { width: 40px; height: 40px; }
  .back-brand .brand-name { font-size: 34px; }
  .tagline {
    position: absolute; left: 46px; top: 124px;
    font-style: italic; font-size: 19px; color: var(--ink-blue);
  }
  .credentials {
    position: absolute; left: 46px; bottom: 46px;
    font-size: 17px; color: var(--ink-blue); line-height: 1.45;
  }
</style>
</head>
<body>

  <section class="card card-front" aria-label="Business card front">
    <div class="front-sky" role="img" aria-label="Soft blue sky with light clouds"></div>
    <div class="front-brand">
      <span class="brand-dot"></span>
      <span class="brand-name">BrightLoft Aerial</span>
    </div>
    <div class="front-info">
      <h1 class="person-name">Marcus Delaney</h1>
      <p class="person-role">Pilot / Owner</p>
      <p class="address">18 Pelmont Ridge<br>Alder Crossing, CT 06000</p>
      <ul class="contact-list">
        <li class="contact-item">
          <svg viewBox="0 0 24 24" aria-hidden="true"><path fill="#ed232b" d="M6.6 10.8a15 15 0 0 0 6.6 6.6l2.2-2.2a1 1 0 0 1 1-.25 11.4 11.4 0 0 0 3.6.57 1 1 0 0 1 1 1V20a1 1 0 0 1-1 1A17 17 0 0 1 3 4a1 1 0 0 1 1-1h3.5a1 1 0 0 1 1 1c0 1.25.2 2.45.57 3.57a1 1 0 0 1-.25 1z"/></svg>
          <span>(203) 555-0147</span>
        </li>
        <li class="contact-item">
          <svg viewBox="0 0 24 24" aria-hidden="true"><rect x="2" y="5" width="20" height="14" rx="1" fill="#ed232b"/><path d="M2 6l10 7 10-7" fill="none" stroke="#fff" stroke-width="1.6"/></svg>
          <span>brightloftaerial@mailbox-example.com</span>
        </li>
        <li class="contact-item">
          <svg viewBox="0 0 24 24" aria-hidden="true"><circle cx="12" cy="12" r="10" fill="#ed232b"/><path d="M2 12h20M12 2c3 3 3 17 0 20M12 2c-3 3-3 17 0 20" fill="none" stroke="#fff" stroke-width="1.3"/></svg>
          <span>brightloftaerial-example.com</span>
        </li>
      </ul>
    </div>
    <div class="front-band"></div>
  </section>

  <section class="card card-back" aria-label="Business card back">
    <div class="back-sky" role="img" aria-label="Soft blue sky with light clouds"></div>
    <div class="back-drone" role="img" aria-label="Photo of a Veltro Hawk 3 drone in flight with camera"></div>
    <div class="back-brand">
      <span class="brand-dot"></span>
      <span class="brand-name">BrightLoft Aerial</span>
    </div>
    <p class="tagline">We'll get the shot you need</p>
    <p class="credentials">FAA 107 # 5164273<br>Insured | Rotor Academy Certified</p>
  </section>

</body>
</html>
```